" É uma lavanderia que atende variados segmentos, lavanderia doméstica, restaurantes, hoteis, indústrias, empresas de segurança, clinicas de estética, cerimonial, casa de repouso... dentre outros. "

```html
<!DOCTYPE html>
<html lang="pt-BR">
<head>
<meta charset="utf-8">
<title>Alvura Lavanderia</title>
<link href="https://fonts.googleapis.com/css2?family=Open+Sans:wght@400;600;700;800&display=swap" rel="stylesheet">
<style>
:root{
  --navy:#0b2a5b;
  --navy-deep:#06193a;
  --blue:#1c6fd6;
  --blue-bright:#2a8af0;
  --cyan:#18b4d8;
  --ink:#333a44;
  --muted:#7a818b;
  --line:#dfe3e8;
  --white:#ffffff;
}
*{margin:0;padding:0;box-sizing:border-box}
html,body{width:1200px;height:1200px;overflow:hidden;background:var(--white);font-family:"Open Sans",Arial,sans-serif;color:var(--ink)}
.page{position:relative;width:1200px;height:1200px}
.col{position:absolute;left:280px;width:640px}

/* header */
.header{top:0;height:84px}
.brand{position:absolute;left:10px;top:22px;display:flex;align-items:center;gap:10px}
.brand-mark{width:40px;height:40px;border-radius:50%;background:var(--blue);flex:none}
.brand-name{font-size:26px;font-weight:700;color:var(--navy);letter-spacing:-.3px}
.header-phone{position:absolute;right:12px;top:18px;font-size:11px;color:var(--ink);display:flex;align-items:center;gap:5px}
.header-tools{position:absolute;right:12px;top:42px;display:flex;align-items:center;gap:5px}
.social{width:18px;height:18px;border-radius:50%;background:var(--navy)}
.search{display:flex;margin-left:8px}
.search-field{width:120px;height:22px;border:1px solid var(--line);font-size:12px;font-style:italic;color:var(--muted);padding:3px 8px}
.search-btn{width:24px;height:22px;background:var(--navy);display:flex;align-items:center;justify-content:center}

.nav{top:84px;height:30px;background:var(--navy);display:flex;align-items:center;padding-left:14px;gap:0}
.nav a{color:var(--white);text-decoration:none;font-size:15px;padding:0 12px;border-right:1px solid rgba(255,255,255,.3);line-height:16px}
.nav a:last-child{border-right:0}
.nav a.active{color:var(--blue-bright)}

/* hero */
.hero{top:114px;height:250px;overflow:hidden}
.hero-panel{position:absolute;left:0;top:0;width:360px;height:250px;background:linear-gradient(90deg,var(--blue) 0%,var(--blue-bright) 100%);padding:44px 0 0 16px;color:var(--white)}
.hero-kicker{font-size:16px;font-weight:600}
.hero-title{font-size:30px;font-weight:700;line-height:36px}
.hero-text{font-size:8.5px;line-height:11px;width:250px;margin-top:6px;opacity:.9;text-transform:uppercase}
.hero-btn{display:inline-block;margin-top:12px;background:var(--white);color:var(--blue);font-size:10px;padding:4px 16px}
.hero-photo{position:absolute;left:330px;top:0;width:310px;height:250px;background:linear-gradient(100deg,rgba(42,138,240,0) 0%,#e9edf2 18%,#c8d0db 50%,#2a3e66 72%,#1a2a4e 100%)}
.hero-dots{top:334px;height:20px;display:flex;gap:6px;align-items:center;padding-left:14px}
.dot{width:10px;height:10px;border-radius:50%;background:#9aa6b4}
.dot.on{width:14px;height:14px;border:2px solid #9aa6b4;background:var(--white)}

/* section heading */
.sec-head{display:flex;align-items:center;justify-content:space-between;height:22px}
.sec-title{display:flex;align-items:center;gap:6px;font-size:16px;font-weight:700;color:var(--navy)}
.sec-icon{width:16px;height:16px;border-radius:50%;background:var(--blue)}
.sec-more{font-size:12px;color:var(--muted);display:flex;align-items:center;gap:5px}

.services-head{top:386px}
.services{top:420px;height:116px;display:flex;gap:8px}
.tile{position:relative;width:100px;height:116px;overflow:hidden}
.tile-photo{position:absolute;inset:0}
.tile-label{position:absolute;left:0;bottom:10px;background:var(--navy);color:var(--white);font-size:9.5px;padding:3px 5px;white-space:nowrap}
.tile-all{background:var(--navy);color:var(--white);padding:10px 8px;text-align:center;width:92px}
.tile-all h4{font-size:11px;font-weight:700;line-height:13px}
.tile-all p{font-size:7.5px;line-height:10px;margin-top:6px;opacity:.85}

/* tips & chat */
.tips{top:562px;width:290px}
.tip{display:flex;gap:8px;margin-top:10px}
.tip-photo{width:56px;height:54px;flex:none}
.tip h5{font-size:10.5px;color:var(--navy);font-weight:600}
.tip p{font-size:8px;line-height:11px;color:var(--muted);margin-top:2px}
.chat{top:562px;left:580px;width:340px}
.chat-body{padding:6px 0 0 24px}
.chat-lead{font-size:13px;line-height:16px;color:var(--ink)}
.chat-hours{font-size:10.5px;line-height:14px;color:var(--muted);margin-top:10px}
.chat-btn{display:inline-block;margin-top:10px;background:var(--navy);color:var(--white);font-size:10px;font-weight:600;padding:6px 14px}

/* banner */
.banner{top:746px;height:112px;display:flex}
.banner-photo{position:relative;width:420px;height:112px;background:linear-gradient(90deg,#5b6068 0%,#8c929b 60%,#a9afb7 100%);padding:20px 0 0 26px}
.banner-line{font-size:25px;font-weight:700;color:var(--white);line-height:32px}
.banner-logo{width:220px;background:var(--navy);display:flex;align-items:center;justify-content:center;gap:10px}
.banner-logo .brand-mark{width:34px;height:34px;background:var(--white)}
.banner-logo span{font-size:22px;font-weight:700;color:var(--white);line-height:26px}

/* clients */
.clients-head{top:884px}
.clients{top:926px;height:50px;display:flex;align-items:center;justify-content:space-between;padding:0 4px}
.client{font-size:24px;font-weight:700;color:#8a9099}

/* footer */
.footer-band{position:absolute;left:0;top:1008px;width:1200px;height:50px;background:linear-gradient(180deg,#3fd0ec 0%,var(--cyan) 40%,#0f8fb8 100%)}
.footer-nav{position:absolute;left:280px;top:1028px;width:640px;display:flex;justify-content:center}
.footer-nav a{color:var(--navy-deep);text-decoration:none;font-size:15px;padding:0 20px;border-right:1px solid rgba(6,25,58,.35);line-height:16px}
.footer-nav a:last-child{border-right:0}
.footer{position:absolute;left:0;top:1058px;width:1200px;height:142px;background:var(--navy-deep)}
.footer-brand{position:absolute;left:280px;top:26px;width:220px;display:flex;align-items:center;gap:10px}
.footer-brand .brand-mark{background:var(--white);width:40px;height:40px}
.footer-brand span{font-size:22px;font-weight:700;color:var(--white);line-height:26px}
.copy{position:absolute;left:284px;top:96px;font-size:9px;color:#b9c3d3}
.contact{position:absolute;left:532px;top:22px;width:400px;color:var(--white)}
.contact h3{font-size:17px;font-weight:600}
.contact-grid{display:grid;grid-template-columns:200px 200px;row-gap:6px;margin-top:10px;font-size:8.5px;color:#c8d1de}
.contact-item{display:flex;gap:5px;align-items:flex-start;line-height:11px}
.contact-item svg{flex:none;margin-top:1px}
.footer-social{display:flex;gap:4px;margin-top:8px}
.footer-social .social{background:var(--white);width:14px;height:14px}
</style>
</head>
<body>
<div class="page">

  <header class="col header">
    <div class="brand"><div class="brand-mark"></div><span class="brand-name">Alvura Lavanderia</span></div>
    <div class="header-phone">
      <svg width="10" height="10" viewBox="0 0 10 10"><path d="M2 1l2 2-1 1.2c.6 1.2 1.6 2.2 2.8 2.8L7 6l2 2-1.2 1.5C4.5 9.3.7 5.5.5 2.2z" fill="#0b2a5b"/></svg>
      Fone: (11) 3000-4821
    </div>
    <div class="header-tools">
      <span class="social"></span><span class="social"></span><span class="social"></span><span class="social"></span>
      <div class="search">
        <div class="search-field">Pesquisar</div>
        <div class="search-btn"><svg width="12" height="12" viewBox="0 0 12 12"><circle cx="5" cy="5" r="3.5" stroke="#fff" stroke-width="1.6" fill="none"/><path d="M7.6 7.6L11 11" stroke="#fff" stroke-width="1.8"/></svg></div>
      </div>
    </div>
  </header>

  <nav class="col nav">
    <a class="active">Home</a><a>Sobre nós</a><a>Serviços</a><a>Meio ambiente</a><a>Dicas</a><a>Contato</a>
  </nav>

  <section class="col hero">
    <div class="hero-photo" role="img" aria-label="Foto de camisa branca com gravata azul escura de bolinhas"></div>
    <div class="hero-panel">
      <div class="hero-kicker">Consulte nossos pacotes para</div>
      <div class="hero-title">Camisas e ternos</div>
      <p class="hero-text">Lavamos camisas e ternos com cuidado profissional, passadoria impecável e entrega rápida para sua rotina. Confira planos mensais.</p>
      <span class="hero-btn">Saiba mais</span>
    </div>
  </section>
  <div class="col hero-dots"><span class="dot on"></span><span class="dot"></span><span class="dot"></span></div>

  <div class="col sec-head services-head">
    <div class="sec-title"><span class="sec-icon"></span>Serviços</div>
    <div class="sec-more">Ver todos os serviços
      <svg width="14" height="10" viewBox="0 0 14 10"><path d="M1 1l4 4-4 4M7 1l4 4-4 4" stroke="#7a818b" stroke-width="1.5" fill="none"/></svg></div>
  </div>
  <section class="col services">
    <div class="tile"><div class="tile-photo" role="img" aria-label="Foto de mesa de cerimonial decorada" style="background:linear-gradient(160deg,#e8d9c4,#9c8466)"></div><span class="tile-label">Cerimonial</span></div>
    <div class="tile"><div class="tile-photo" role="img" aria-label="Foto de salão de restaurante" style="background:linear-gradient(160deg,#c98a4a,#5a3218)"></div><span class="tile-label">Restaurante</span></div>
    <div class="tile"><div class="tile-photo" role="img" aria-label="Foto de tratamento em clínica de estética" style="background:linear-gradient(160deg,#f1d6c6,#c08f78)"></div><span class="tile-label">Clínica de estética</span></div>
    <div class="tile"><div class="tile-photo" role="img" aria-label="Foto de pet shop" style="background:linear-gradient(160deg,#d9a25a,#7a4c22)"></div><span class="tile-label">Pet shop</span></div>
    <div class="tile"><div class="tile-photo" role="img" aria-label="Foto de quarto de hotel" style="background:linear-gradient(160deg,#d8b47c,#6d4a26)"></div><span class="tile-label">Hotel</span></div>
    <div class="tile tile-all"><h4>Empresas em Geral</h4><p>Atendemos indústrias, segurança, casas de repouso e muito mais.</p></div>
  </section>

  <section class="col tips">
    <div class="sec-head"><div class="sec-title"><span class="sec-icon"></span>Dicas de lavanderia</div></div>
    <div class="tip">
      <div class="tip-photo" role="img" aria-label="Foto de roupas limpas e dobradas" style="background:linear-gradient(150deg,#f0e6dc,#b89c84)"></div>
      <div><h5>Oito dicas para ter roupas limpas</h5><p>Separe peças por cor e tecido, leia as etiquetas e use água na temperatura indicada.</p></div>
    </div>
    <div class="tip">
      <div class="tip-photo" role="img" aria-label="Foto de roupas limpas e dobradas" style="background:linear-gradient(150deg,#f0e6dc,#b89c84)"></div>
      <div><h5>Oito dicas para ter roupas limpas</h5><p>Separe peças por cor e tecido, leia as etiquetas e use água na temperatura indicada.</p></div>
    </div>
  </section>

  <section class="col chat">
    <div class="sec-head"><div class="sec-title"><span class="sec-icon"></span>Chat online</div></div>
    <div class="chat-body">
      <p class="chat-lead">Fale com algum dos nossos especialistas para tirar dúvidas ou fazer sugestões, teremos enorme prazer em atendê-lo.</p>
      <p class="chat-hours">Segunda à Sexta das 07h45 às 20h00<br>Sábados das 08h00 às 12h00</p>
      <span class="chat-btn">Acessar chat</span>
    </div>
  </section>

  <section class="col banner">
    <div class="banner-photo" role="img" aria-label="Foto de pessoa de terno ajustando a gravata">
      <div class="banner-line">Faça um</div>
      <div class="banner-line">Orçamento conosco</div>
    </div>
    <div class="banner-logo"><div class="brand-mark"></div><span>Alvura<br>Lavanderia</span></div>
  </section>

  <div class="col sec-head clients-head">
    <div class="sec-title"><span class="sec-icon"></span>Clientes</div>
    <div class="sec-more">Ver todos os clientes
      <svg width="14" height="10" viewBox="0 0 14 10"><path d="M1 1l4 4-4 4M7 1l4 4-4 4" stroke="#7a818b" stroke-width="1.5" fill="none"/></svg></div>
  </div>
  <div class="col clients">
    <span class="client">Viajora</span><span class="client">Motrix</span><span class="client">Ampla</span><span class="client">Tecnova</span>
  </div>

  <div class="footer-band"></div>
  <nav class="footer-nav"><a>Home</a><a>Sobre nós</a><a>Serviços</a><a>Meio ambiente</a><a>Dicas</a><a>Contato</a></nav>

  <footer class="footer">
    <div class="footer-brand"><div class="brand-mark"></div><span>Alvura<br>Lavanderia</span></div>
    <p class="copy">Copyright © 2014 Estúdio Nova</p>
    <div class="contact">
      <h3>Contato</h3>
      <div class="contact-grid">
        <div class="contact-item"><svg width="10" height="8" viewBox="0 0 10 8"><rect x=".5" y=".5" width="9" height="7" fill="none" stroke="#fff"/><path d="M.5 .5L5 4.5 9.5 .5" fill="none" stroke="#fff"/></svg>Email: contato@alvuralavanderia.com.br</div>
        <div class="contact-item"><svg width="10" height="10" viewBox="0 0 10 10"><circle cx="5" cy="5" r="4.2" fill="none" stroke="#fff"/><path d="M1 5h8M5 1v8" stroke="#fff" stroke-width=".8"/></svg>Site: www.alvuralavanderia.com.br</div>
        <div class="contact-item"><svg width="10" height="10" viewBox="0 0 10 10"><path d="M2 1l2 2-1 1.2c.6 1.2 1.6 2.2 2.8 2.8L7 6l2 2-1.2 1.5C4.5 9.3.7 5.5.5 2.2z" fill="#fff"/></svg>Fone: (11) 3000-4822 / (11) 3000-4822</div>
        <div class="contact-item"><svg width="8" height="11" viewBox="0 0 8 11"><path d="M4 10.5S.5 6.4.5 4a3.5 3.5 0 017 0c0 2.4-3.5 6.5-3.5 6.5z" fill="#fff"/><circle cx="4" cy="4" r="1.3" fill="#06193a"/></svg>Rua das Acácias, 120<br>Jardim Aurora - São Paulo - SP</div>
      </div>
      <div class="footer-social"><span class="social"></span><span class="social"></span><span class="social"></span><span class="social"></span></div>
    </div>
  </footer>

</div>
</body>
</html>
```